New Business Cards for 3 companies - print and digital Needed FAST!

We have rebranded our company into three separate companies.
We need new business cards for 8 employees, three of whom need a business card for each company - total of 12 cards.
Pelmary is our property development company.
Velta Brokerage & Management handles property management and real estate transactions.
Oakwren Design Build is our construction company.
Business cards MUST be able to be both printed and function as digital business cards.
No black backgrounds.
Front should be each employee's information and include the logo from their primary company.
Back should include all three logos.
Please see the uploaded spreadsheet for all the information you need for each card. Also uploaded the .png files for each logo as well as the style guide for each logo.

Contact Information for Business Card

See uploaded spreadsheet for information

Font styles to use
Sans Serif
Other font styles liked:
• match style guide if possible

Requirements
Should not have
• No dark backgrounds on the front (on the back OK.) No pictures of employees. Thanks!

```html
<!DOCTYPE html>
<html lang="en">
<head>
<meta charset="utf-8">
<title>Oakwren Design Build – Business Card</title>
<link href="https://fonts.googleapis.com/css2?family=Michroma&family=Roboto+Condensed:wght@400;500&family=Roboto:wght@500;700&display=swap" rel="stylesheet">
<style>
  :root {
    --backdrop: #e7e4df;
    --card-white: #ffffff;
    --card-dark: #454545;
    --ink: #474747;
    --blue: #1f77c0;
    --strip: #3d3d3d;
    --white: #ffffff;
  }
  * { margin: 0; padding: 0; box-sizing: border-box; }
  html, body { width: 900px; height: 1200px; overflow: hidden; }
  body { background: var(--backdrop); position: relative; font-family: "Roboto Condensed", sans-serif; }

  .card {
    position: absolute; left: 82px; width: 733px; height: 428px;
    border-radius: 22px; overflow: hidden;
    box-shadow: 0 8px 18px rgba(0,0,0,0.25);
  }
  .card-front { top: 138px; background: var(--card-white); }
  .card-back { top: 634px; background: var(--card-dark); }

  .holder { position: absolute; left: 40px; top: 66px; font-family: "Michroma", sans-serif; }
  .holder-name { font-size: 17px; letter-spacing: 1.5px; color: var(--ink); }
  .holder-title { font-size: 14px; letter-spacing: 1px; color: var(--blue); margin-top: 6px; }

  .company-mark {
    position: absolute; right: 42px; top: 80px; text-align: right;
    font-family: "Michroma", sans-serif; color: var(--blue); line-height: 1.15;
  }
  .company-mark .mark-name { font-size: 36px; letter-spacing: 1px; }
  .company-mark .mark-sub { font-size: 16px; letter-spacing: 4px; margin-top: 14px; }

  .rule { position: absolute; top: 282px; height: 3px; }
  .rule-dark { left: 40px; width: 428px; background: var(--strip); }
  .rule-blue { left: 478px; width: 213px; background: var(--blue); }

  .contacts { position: absolute; left: 40px; top: 302px; list-style: none; }
  .contacts li, .address { display: flex; align-items: flex-start; font-size: 16px; color: var(--ink); height: 25px; }
  .contacts svg { width: 14px; height: 14px; margin: 3px 11px 0 0; flex: none; }
  .address { position: absolute; left: 478px; top: 302px; height: auto; line-height: 25px; }
  .address svg { width: 14px; height: 18px; margin: 3px 11px 0 0; flex: none; }

  .bottom-strip { position: absolute; left: 0; bottom: 0; width: 100%; height: 13px; background: var(--strip); }
  .web-tab { position: absolute; right: 0; bottom: 0; width: 320px; height: 30px; }
  .web-tab svg.tab-shape { position: absolute; inset: 0; }
  .web-link {
    position: absolute; left: 56px; top: 6px; display: flex; align-items: center;
    font-family: "Roboto", sans-serif; font-weight: 700; font-size: 15px; letter-spacing: 0.5px; color: var(--white);
  }
  .web-link svg { width: 14px; height: 14px; margin-right: 9px; }

  .brand {
    position: absolute; top: 198px; width: 200px; text-align: center;
    font-family: "Michroma", sans-serif; color: var(--white); font-size: 20px; letter-spacing: 1px; line-height: 30px;
  }
  .brand-pelmary { left: 86px; }
  .brand-velta { left: 321px; }
  .brand-oakwren { left: 500px; }
</style>
</head>
<body>

<section class="card card-front" aria-label="Business card front">
  <div class="holder">
    <p class="holder-name">DANIEL MARSH</p>
    <p class="holder-title">CEO / OWNER</p>
  </div>

  <div class="company-mark">
    <p class="mark-name">OAKWREN</p>
    <p class="mark-sub">DESIGN | BUILD</p>
  </div>

  <div class="rule rule-dark"></div>
  <div class="rule rule-blue"></div>

  <ul class="contacts">
    <li>
      <svg viewBox="0 0 14 14"><rect x="3" y="0.8" width="8" height="12.4" rx="1.5" fill="none" stroke="var(--blue)" stroke-width="1.6"/><rect x="6" y="10.6" width="2" height="1.2" fill="var(--blue)"/></svg>
      555-201-4830
    </li>
    <li>
      <svg viewBox="0 0 14 14"><path d="M3 1.5l2.2 2.6-1.2 1.6c.8 1.8 2.3 3.3 4.1 4.1l1.6-1.2 2.6 2.2-1.3 2C6 12.6 1.4 8 1 2.8z" fill="var(--blue)"/></svg>
      555-209-7714 x101
    </li>
    <li>
      <svg viewBox="0 0 14 14"><rect x="0.5" y="2.5" width="13" height="9" fill="var(--blue)"/><path d="M0.8 3l6.2 5 6.2-5" fill="none" stroke="var(--white)" stroke-width="1.2"/></svg>
      dmarsh@pelmary.com
    </li>
  </ul>

  <p class="address">
    <svg viewBox="0 0 14 18"><path d="M7 0.5a6 6 0 0 1 6 6c0 4.5-6 11-6 11S1 11 1 6.5a6 6 0 0 1 6-6z" fill="var(--blue)"/><circle cx="7" cy="6.5" r="2.3" fill="var(--white)"/></svg>
    <span>48 N. Linden Ave., Ste 3B,<br>Ashford IL 60590</span>
  </p>

  <div class="bottom-strip"></div>
  <div class="web-tab">
    <svg class="tab-shape" viewBox="0 0 320 30" preserveAspectRatio="none">
      <polygon points="0,30 20,2 320,2 320,30" fill="var(--blue)"/>
      <polygon points="24,0 320,0 320,2 22,2" fill="var(--white)"/>
    </svg>
    <p class="web-link">
      <svg viewBox="0 0 14 14" fill="none" stroke="var(--white)" stroke-width="1.2"><circle cx="7" cy="7" r="6"/><ellipse cx="7" cy="7" rx="2.6" ry="6"/><path d="M1 7h12M2 3.8h10M2 10.2h10"/></svg>
      WWW.OAKWRENBUILD.COM
    </p>
  </div>
</section>

<section class="card card-back" aria-label="Business card back">
  <p class="brand brand-pelmary">PELMARY</p>
  <p class="brand brand-velta">VELTA</p>
  <p class="brand brand-oakwren">OAKWREN</p>
</section>

</body>
</html>
```